catering postcard

We need a postcard that lets offices know that we cater and can deliver our delicious food to their office/meeting/event.

We are a mom and pop, super busy, well-loved Italian restaurant.
(check us out at pennysbistrokitchen.com)

The final design should communicate delicious food, brought to your place of work. It arrives on time and is hot and ready to be devoured.

We'd like to see bright colors and a huge impact on our lunch time catering sales.

Catering

```html
<!DOCTYPE html>
<html lang="en">
<head>
<meta charset="utf-8">
<title>Penny's Bistro Kitchen – Catering Postcard</title>
<link href="https://fonts.googleapis.com/css2?family=Arimo:wght@400;700&family=Tinos:ital,wght@0,400;0,700;1,400&display=swap" rel="stylesheet">
<style>
  :root{
    --green:#1f8a3b;
    --red:#c8102e;
    --white:#ffffff;
    --ink:#2b2b2b;
    --line:#b9b9b9;
    --backdrop:#e9e9e9;
  }
  *{box-sizing:border-box;margin:0;padding:0}
  html,body{width:1200px;height:625px;overflow:hidden;background:var(--backdrop)}
  .canvas{position:relative;width:1200px;height:625px}
  .postcard{position:absolute;top:122px;width:570px;height:380px;background:var(--white);overflow:hidden;box-shadow:0 2px 10px rgba(0,0,0,.18)}
  .postcard--front{left:20px}
  .postcard--back{left:610px}
  .postcard svg{position:absolute;inset:0;width:100%;height:100%}

  .brand{position:absolute;display:flex;align-items:center;gap:8px;white-space:nowrap}
  .brand__dot{width:11px;height:11px;border-radius:50%;background:var(--red)}
  .brand__name{font-family:"Tinos",serif;font-weight:700;color:var(--green);line-height:1}
  .brand__tagline{position:absolute;font-family:"Tinos",serif;font-style:italic;color:var(--red);font-size:13px;white-space:nowrap}

  .front .brand{left:176px;top:30px}
  .front .brand__name{font-size:24px}
  .front .brand__tagline{left:214px;top:62px}

  .ribbon{position:absolute;left:450px;top:0;width:108px;height:128px;background:var(--red);clip-path:polygon(0 0,100% 0,100% 100%,50% 88%,0 100%);z-index:2}
  .ribbon-text{position:absolute;left:6px;top:8px;width:98px;font-family:"Tinos",serif;color:var(--white);font-size:12.5px;line-height:1.2}
  .ribbon-text::first-letter{font-size:17px}

  .quote{position:absolute;left:26px;top:298px;width:340px;font-family:"Tinos",serif;font-style:italic;color:var(--ink);font-size:12.5px;line-height:1.3}

  .back .brand{left:24px;top:40px}
  .back .brand__name{font-size:30px}
  .back .brand__tagline{left:62px;top:76px}

  .pitch{position:absolute;left:20px;top:170px;width:280px;font-family:"Arimo",sans-serif;color:var(--white)}
  .pitch__lead{font-size:14px;line-height:1.25}
  .pitch__lead .initial{color:var(--red);font-size:19px;font-weight:700}
  .pitch__cta{margin-top:10px;font-size:15px;font-weight:700}
  .pitch__address{margin-top:4px;font-size:11.5px;line-height:1.3}
</style>
</head>
<body>
<main class="canvas">

  <section class="postcard postcard--front front" aria-label="Postcard front">
    <svg viewBox="0 0 570 380" preserveAspectRatio="none" aria-hidden="true">
      <path d="M0,0 H130 C90,20 40,45 0,75 Z" fill="var(--green)"/>
      <path d="M0,104 C100,88 200,92 300,110 C400,128 480,122 570,104" fill="none" stroke="var(--red)" stroke-width="12"/>
      <path d="M0,118 C100,102 200,106 300,124 C400,142 480,136 570,118" fill="none" stroke="var(--green)" stroke-width="3"/>
      <path d="M0,250 C180,272 380,268 570,232 V248 C380,284 180,288 0,266 Z" fill="var(--red)"/>
      <path d="M330,380 C430,356 500,326 570,286 V380 Z" fill="var(--green)"/>
    </svg>
    <svg viewBox="0 0 570 380" preserveAspectRatio="none" role="img" aria-label="Photo of ribbon pasta with shrimp, cherry tomatoes and fresh herbs">
      <defs>
        <clipPath id="plate-shape"><path d="M0,124 C100,108 200,112 300,130 C400,148 480,142 570,124 V232 C380,268 180,272 0,250 Z"/></clipPath>
        <linearGradient id="plate-tones" x1="0" y1="0" x2="1" y2="1">
          <stop offset="0" stop-color="#e8c98f"/>
          <stop offset=".4" stop-color="#f1dcae"/>
          <stop offset=".7" stop-color="#d9a36a"/>
          <stop offset="1" stop-color="#c2452f"/>
        </linearGradient>
      </defs>
      <rect width="570" height="380" fill="url(#plate-tones)" clip-path="url(#plate-shape)"/>
    </svg>

    <div class="brand"><span class="brand__dot"></span><span class="brand__name">Penny's Bistro Kitchen</span></div>
    <p class="brand__tagline">Pizza, Pasta &amp; Caffè</p>
    <div class="ribbon"><p class="ribbon-text">We cater and can deliver delicious Italian meals to your office, meeting, event etc.</p></div>
    <p class="quote">"Here at Penny's, we manage our menu closely to provide our customers with quality and delicious meals. Our daily specials reflect the seasons and availability of fresh local and regional produce."&nbsp; Buon Appetito !</p>
  </section>

  <section class="postcard postcard--back back" aria-label="Postcard back">
    <svg viewBox="0 0 570 380" preserveAspectRatio="none" aria-hidden="true">
      <rect x="462" y="18" width="84" height="78" fill="none" stroke="var(--line)" stroke-width="1.5"/>
      <g stroke="var(--line)" stroke-width="1">
        <line x1="385" y1="150" x2="548" y2="150"/>
        <line x1="385" y1="172" x2="548" y2="172"/>
        <line x1="385" y1="194" x2="548" y2="194"/>
        <line x1="385" y1="216" x2="548" y2="216"/>
        <line x1="385" y1="238" x2="548" y2="238"/>
        <line x1="385" y1="260" x2="548" y2="260"/>
        <line x1="385" y1="282" x2="548" y2="282"/>
        <line x1="385" y1="304" x2="548" y2="304"/>
      </g>
      <path d="M0,140 H270 C330,180 350,290 340,380 H0 Z" fill="var(--red)"/>
      <path d="M0,154 H262 C318,192 334,292 326,380 H0 Z" fill="var(--green)"/>
      <path d="M282,140 C370,190 372,300 360,380" fill="none" stroke="var(--red)" stroke-width="6"/>
      <path d="M0,370 H570 V380 H0 Z" fill="var(--green)"/>
    </svg>

    <div class="brand"><span class="brand__dot"></span><span class="brand__name">Penny's Bistro Kitchen</span></div>
    <p class="brand__tagline">Pizza, Pasta &amp; Caffè</p>

    <div class="pitch">
      <p class="pitch__lead"><span class="initial">A</span>re you in need of delicious Italian meals delivered to your office meeting, event etc?</p>
      <p class="pitch__cta">Contact us today!</p>
      <p class="pitch__address">Penny's Bistro Kitchen<br>48 Linden Grove Lane<br>Millbrook, Alabama 35100<br>(205) 555-0142</p>
    </div>
  </section>

</main>
</body>
</html>
```